Stationery for Heating Plumbing & Electrical Contractor
Veltrana
Stationery for Heating Plumbing & Electrical Contractor - Construction
Creative Brief
Professional
Neil Farrow
Director
428b Pellham Rd , Oakvane, Warrington , Cheshire QX7 3PZ
Mornwick@fenmail.com
www.veltrana.uk.com

```html
<!DOCTYPE html>
<html lang="en">
<head>
<meta charset="utf-8">
<title>Veltrana Business Cards</title>
<link rel="stylesheet" href="https://fonts.googleapis.com/css2?family=Montserrat:wght@400;500;600&display=swap">
<style>
  :root {
    --backdrop: #ececec;
    --card-white: #ffffff;
    --card-dark: #3d3d3f;
    --accent: #f6b21b;
    --ink: #4a4a4c;
    --ink-soft: #8a8a8e;
    --name-red: #b8452e;
    --title-blue: #3f5d9a;
    --wordmark-light: #c9c9cc;
  }
  * { margin: 0; padding: 0; box-sizing: border-box; }
  html, body {
    width: 1200px; height: 906px; overflow: hidden;
    background: var(--backdrop);
    font-family: "Montserrat", Arial, sans-serif;
  }
  .canvas {
    position: relative; width: 1200px; height: 906px;
  }
  .card {
    position: absolute; width: 520px; height: 297px;
    top: 305px; box-shadow: 0 6px 18px rgba(0,0,0,0.12);
  }
  .card-front { left: 50px; background: var(--card-white); }
  .card-back { left: 630px; background: var(--card-dark); }

  .brand {
    position: absolute; left: 230px; top: 62px;
    display: flex; align-items: center; gap: 10px;
  }
  .brand-dot {
    width: 30px; height: 30px; border-radius: 50%; background: var(--accent);
  }
  .brand-name {
    font-size: 34px; font-weight: 600; color: var(--ink); letter-spacing: -0.5px;
  }
  .holder {
    position: absolute; left: 244px; top: 118px; text-align: left;
  }
  .holder-name {
    font-size: 12px; font-weight: 600; color: var(--name-red);
    text-transform: uppercase; letter-spacing: 0.5px;
  }
  .holder-title {
    font-size: 10px; font-weight: 500; color: var(--title-blue);
    text-transform: uppercase; letter-spacing: 0.5px; margin-top: 2px;
  }
  .contact-list { position: absolute; list-style: none; }
  .contact-list li {
    display: flex; align-items: center; gap: 7px;
    font-size: 8.5px; color: var(--ink-soft); height: 15px; margin-bottom: 3px;
  }
  .contact-left { left: 22px; top: 76px; }
  .contact-right { left: 230px; top: 196px; }
  .icon {
    width: 12px; height: 12px; background: var(--accent);
    display: inline-flex; align-items: center; justify-content: center; flex-shrink: 0;
  }
  .icon svg { width: 8px; height: 8px; }

  .back-wordmark {
    position: absolute; right: 34px; bottom: 34px;
    font-size: 44px; font-weight: 400; color: var(--wordmark-light); letter-spacing: 1px;
  }
</style>
</head>
<body>
<div class="canvas">

  <section class="card card-front">
    <ul class="contact-list contact-left">
      <li><span class="icon"><svg viewBox="0 0 10 10"><path d="M5 1a3 3 0 0 1 3 3c0 2-3 5-3 5S2 6 2 4a3 3 0 0 1 3-3z" fill="#fff"/></svg></span>428b Pellham Rd</li>
      <li><span class="icon"><svg viewBox="0 0 10 10"><path d="M2 1h2l1 2-1 1a6 6 0 0 0 2 2l1-1 2 1v2c-4 0-7-3-7-7z" fill="#fff"/></svg></span>012 345 6789</li>
      <li><span class="icon"><svg viewBox="0 0 10 10"><rect x="1" y="2.5" width="8" height="5" fill="#fff"/><path d="M1 2.5l4 3 4-3" stroke="#f6b21b" fill="none"/></svg></span>Mornwick@fenmail.com</li>
    </ul>

    <div class="brand">
      <span class="brand-dot"></span>
      <span class="brand-name">Veltrana</span>
    </div>
    <div class="holder">
      <p class="holder-name">Neil Farrow</p>
      <p class="holder-title">President</p>
    </div>

    <ul class="contact-list contact-right">
      <li><span class="icon"><svg viewBox="0 0 10 10"><rect x="1" y="2.5" width="8" height="5" fill="#fff"/><path d="M1 2.5l4 3 4-3" stroke="#f6b21b" fill="none"/></svg></span>Mornwick@fenmail.com</li>
      <li><span class="icon"><svg viewBox="0 0 10 10"><circle cx="5" cy="5" r="3.5" stroke="#fff" fill="none"/><path d="M1.5 5h7M5 1.5v7" stroke="#fff"/></svg></span>www.veltrana.uk.com</li>
      <li><span class="icon"><svg viewBox="0 0 10 10"><circle cx="5" cy="5" r="3.5" stroke="#fff" fill="none"/><path d="M1.5 5h7M5 1.5v7" stroke="#fff"/></svg></span>www.veltrana.uk.com</li>
    </ul>
  </section>

  <section class="card card-back">
    <p class="back-wordmark">veltrana</p>
  </section>

</div>
</body>
</html>
```